Automotive Parts Company Business Card/Logo Design

We need a logo/business card for a new automotive parts and accessories company which is based in Barbados. The company will only have an online presence and this will reduce our overheads and allow us to pass potential savings to our customers.

We will offer most automotive parts which include, but are not limited to, accessories, exterior, interior, body parts.

We want to appeal to a very wide audience and we're looking for a modern, clean and bold design to make the company seem very professional. Our logo and facebook page will be our only customer facing items. So it is essential that these are done correctly.

The design should really communicate that we can provide premium car parts at affordable prices for all types of cars e.g. European and Japanese.

We will stock items and also source hard to get and unique pieces. We aim to not just be another shop that sells parts. But we want to work with our customers to achieve their car goals.

The company name is GearVista and our slogan is Quality Parts At Affordable Prices.
The design should be very modern, clean and bold.

I've included examples of some of the business cards I like as well as images of car products.
Updates

Dear Designers,

I've uploaded some samples of some business card/logo designs I like. Please have a look at the project brief. Just to reiterate, I am looking for a clean, modern design.

Thanks,

Rohan

Dear Designers,

Please note the Apr 14th deadline is soon approaching.

Also note the business card is double-sided.

I look forward to working with you.

Thanks,

Rohan

Target Market(s)

20 - 30 (young professionals, younger generation with disposible income) and then then all other markets

Industry/Entity Type

Automotive

Contact Information for Business Card

Rohan Melwanikar
GearVista
Quality Parts At Affordable Prices
https://www.examplesocial.test/gearvistabq
246-319-8042
gearvistabq@mailbox-example.test

```html
<!DOCTYPE html>
<html lang="en">
<head>
<meta charset="utf-8">
<title>GearVista Business Card</title>
<link rel="stylesheet" href="https://fonts.googleapis.com/css2?family=Open+Sans:wght@400;600&display=swap">
<style>
  :root {
    --page-bg: #e9e6e2;
    --card-white: #ffffff;
    --ink: #2b2b2b;
    --ink-soft: #3c3c3c;
    --brand-blue: #1f6fe0;
    --band-dark: #2a2a2c;
    --card-black: #0b0b0c;
    --name-on-dark: #f2f2f2;
    --slogan: #f2f2f2;
  }
  * { box-sizing: border-box; margin: 0; padding: 0; }
  html, body {
    width: 924px; height: 1200px; overflow: hidden;
    background: var(--page-bg);
    font-family: "Open Sans", Arial, sans-serif;
  }
  .sheet { position: relative; width: 924px; height: 1200px; }
  .card {
    position: absolute; left: 112px; width: 700px; height: 400px;
    border-radius: 4px; overflow: hidden;
    box-shadow: 0 10px 28px rgba(0,0,0,0.18);
  }
  /* Front side */
  .card--front { top: 140px; background: var(--card-white); }
  .company-name {
    font-weight: 600; letter-spacing: 0; text-transform: none;
  }
  .card--front .company-name {
    position: absolute; top: 52px; left: 300px;
    font-size: 28px; color: var(--ink);
  }
  .card--front .person {
    position: absolute; top: 118px; left: 300px;
    font-size: 24px; font-weight: 400; color: var(--ink);
  }
  .contacts {
    position: absolute; top: 166px; left: 300px;
    list-style: none; font-size: 16px; color: var(--ink-soft);
  }
  .contacts li { display: flex; align-items: center; gap: 10px; height: 30px; }
  .contacts .icon { width: 16px; height: 16px; flex: none; }
  .contacts .social-square {
    width: 14px; height: 14px; background: var(--brand-blue);
    border-radius: 2px; flex: none; margin: 0 1px;
  }
  .card--front .rule {
    position: absolute; left: 0; right: 0; top: 292px; height: 5px;
    background: var(--brand-blue);
  }
  .card--front .band {
    position: absolute; left: 0; right: 0; top: 297px; bottom: 0;
    background: var(--band-dark);
    display: flex; align-items: center; padding-left: 60px;
  }
  .slogan { color: var(--slogan); font-size: 25px; font-weight: 400; }
  /* Back side */
  .card--back {
    top: 660px;
    background: radial-gradient(ellipse at 45% 40%, #1d1d20 0%, var(--card-black) 70%);
    display: flex; align-items: center; justify-content: center;
  }
  .card--back .company-name { font-size: 40px; color: var(--name-on-dark); }
</style>
</head>
<body>
<main class="sheet">
  <section class="card card--front" aria-label="Business card front">
    <div class="company-name">GearVista</div>
    <div class="person">Rohan Melwanikar</div>
    <ul class="contacts">
      <li>
        <svg class="icon" viewBox="0 0 24 24" aria-hidden="true"><path fill="#1f6fe0" d="M6.6 10.8a15 15 0 0 0 6.6 6.6l2.2-2.2a1 1 0 0 1 1-.25 11.4 11.4 0 0 0 3.6.6 1 1 0 0 1 1 1V20a1 1 0 0 1-1 1A17 17 0 0 1 3 4a1 1 0 0 1 1-1h3.5a1 1 0 0 1 1 1c0 1.25.2 2.45.6 3.6a1 1 0 0 1-.25 1z"/></svg>
        <span>246-319-8042</span>
      </li>
      <li>
        <svg class="icon" viewBox="0 0 24 24" aria-hidden="true"><rect x="2" y="5" width="20" height="14" rx="1" fill="#1f6fe0"/><path d="M3 6l9 7 9-7" fill="none" stroke="#fff" stroke-width="1.6"/></svg>
        <span>gearvistabq@mailbox-example.test</span>
      </li>
      <li>
        <span class="social-square" aria-hidden="true"></span>
        <span>www.examplesocial.test/gearvistabq</span>
      </li>
    </ul>
    <div class="rule"></div>
    <div class="band"><p class="slogan">Quality Parts At Affordable Prices</p></div>
  </section>

  <section class="card card--back" aria-label="Business card back">
    <div class="company-name">GearVista</div>
  </section>
</main>
</body>
</html>
```